A register your interest postcard

It is a slightly bigger postcard that wil be inserted inside a brochure. On one side it is to have the logo with the statement "at Quillory, Byron Bay" underneath. At the bottom it is to say "Register your interest to become an owner at The Harbourmark Circle. On the flipside it has the logo in a smaller version with again in smaller writing "Become an owner at The Harbourmark Circle". The main point of this side it to say " SMS your name to 0481 552 903 OR Name: Email: Phone:".
I would like a wood-look style postcard. It is for a luxury beach property that uses a lot of distressed wood in the building of the houses.
I would like a wood-look style postcard for a beach property.

```html
<!DOCTYPE html>
<html lang="en">
<head>
<meta charset="utf-8">
<title>Register Your Interest Postcard – The Harbourmark Circle</title>
<link rel="stylesheet" href="https://fonts.googleapis.com/css2?family=Poppins:wght@600;700&display=swap">
<style>
  :root {
    --wood-light: #d2b48c;
    --wood-mid: #b8956a;
    --wood-dark: #8f6f4c;
    --wood-shade: #7a5c3d;
    --logo-ink: #3e3c3a;
    --tagline: #ffffff;
    --band: #ffffff;
    --band-text: #a08b63;
    --trim-line: #e0414b;
  }

  * { margin: 0; padding: 0; box-sizing: border-box; }

  html, body {
    width: 1200px;
    height: 741px;
    overflow: hidden;
    background: #ffffff;
  }

  .postcard {
    position: relative;
    width: 1200px;
    height: 741px;
    font-family: "Poppins", "Century Gothic", sans-serif;
    background: var(--band);
    overflow: hidden;
  }

  .wood-panel {
    position: absolute;
    left: 0;
    top: 0;
    width: 1200px;
    height: 638px;
    background:
      linear-gradient(178deg, rgba(255,255,255,0.08) 0%, rgba(0,0,0,0) 40%, rgba(60,40,20,0.12) 100%),
      linear-gradient(100deg, var(--wood-light) 0%, var(--wood-mid) 45%, var(--wood-dark) 80%, var(--wood-shade) 100%);
  }

  .brand-name {
    position: absolute;
    left: 80px;
    top: 62px;
    color: var(--logo-ink);
    font-weight: 700;
    font-size: 112px;
    line-height: 118px;
    letter-spacing: -1px;
    text-transform: uppercase;
  }

  .brand-name span { display: block; }

  .tagline {
    position: absolute;
    left: 81px;
    top: 434px;
    color: var(--tagline);
    font-weight: 700;
    font-size: 49px;
    line-height: 1.2;
    letter-spacing: -0.5px;
    text-shadow: 2px 2px 3px rgba(40, 28, 15, 0.6);
  }

  .register-band {
    position: absolute;
    left: 0;
    top: 638px;
    width: 1200px;
    height: 103px;
    display: flex;
    align-items: center;
    justify-content: center;
    padding-bottom: 18px;
  }

  .register-band p {
    color: var(--band-text);
    font-weight: 700;
    font-size: 28px;
    letter-spacing: -0.2px;
  }

  .trim-line {
    position: absolute;
    left: 20px;
    top: 22px;
    width: 1160px;
    height: 697px;
    border: 1px dashed var(--trim-line);
    pointer-events: none;
  }
</style>
</head>
<body>
  <main class="postcard">
    <div class="wood-panel" role="img" aria-label="Close-up photograph of weathered, distressed timber grain in warm sand and brown tones"></div>

    <h1 class="brand-name">
      <span>The</span>
      <span>Harbourmark</span>
      <span>Circle</span>
    </h1>

    <p class="tagline">at Quillory, Byron Bay</p>

    <div class="register-band">
      <p>Register your interest to become an owner at The Harbourmark Circle.</p>
    </div>

    <div class="trim-line" aria-hidden="true"></div>
  </main>
</body>
</html>
```